Mini Market Tavo Business Presentation Cards

We need presentation cards with a logo we already own designed at this website as well. We need the printing, delivery and sleek, modem design in harmony with our previous logo design.

Target Market(s)

Low, med and High income class.

Industry/Entity Type

Grocery Store

Contact Information for Business Card

Business logo (Mini Market Tavo), name: Esteban L. Morales/Lidia M. Paz/ Hugo Paz (those are the names for the different cards),
Address: Col. Lomas del Viento, carretera a Tela a 200mts del Centro Comunal. Puerto Cortés, Honduras.
Email: minimarkettavo@correo-ejemplo.hn
Teléfono: (504) 9731-5064

Font styles to use
Serif
Sans Serif

Requirements
Must have
• Business logo (Mini Market Tavo), person name, department,
• Address, phone number, email address.

```html
<!DOCTYPE html>
<html lang="es">
<head>
<meta charset="utf-8">
<title>Mini Market Tavo – Tarjeta de presentación</title>
<link rel="stylesheet" href="https://fonts.googleapis.com/css2?family=Questrial&display=swap">
<style>
  :root{
    --canvas:#ecebe8;
    --card:#ffffff;
    --brand-red:#e4432b;
    --brand-green:#7cb445;
    --band-text:#ffffff;
  }
  *{margin:0;padding:0;box-sizing:border-box}
  html,body{width:1200px;height:1200px;overflow:hidden}
  body{background:var(--canvas);font-family:"Questrial",Arial,sans-serif;position:relative}
  .business-card{
    position:absolute;left:60px;top:285px;width:1080px;height:630px;
    background:var(--card);box-shadow:0 6px 24px rgba(0,0,0,.12);overflow:hidden;
  }
  .card-holder-name{
    position:absolute;top:84px;left:0;right:0;text-align:center;
    color:var(--brand-green);font-size:28px;letter-spacing:.5px;text-transform:uppercase;
  }
  .brand-name{
    position:absolute;top:268px;left:0;right:0;text-align:center;
    color:var(--brand-red);font-size:72px;line-height:1;white-space:nowrap;
  }
  .contact-band{
    position:absolute;left:0;right:0;bottom:0;height:106px;
    background:var(--brand-red);border-top:4px solid var(--brand-green);
    color:var(--band-text);font-size:25px;line-height:1;text-align:center;
    display:flex;flex-direction:column;justify-content:center;gap:10px;
  }
  .contact-line{display:flex;align-items:center;justify-content:center;gap:7px;white-space:nowrap}
  .contact-icon{width:17px;height:22px;flex:none}
</style>
</head>
<body>
  <section class="business-card">
    <p class="card-holder-name">Esteban L. Morales</p>

    <p class="brand-name">Mini Market Tavo</p>

    <footer class="contact-band">
      <p class="contact-line">
        <svg class="contact-icon" viewBox="0 0 16 20" aria-hidden="true"><path d="M8 0a7 7 0 0 0-7 7c0 5 7 13 7 13s7-8 7-13a7 7 0 0 0-7-7z" fill="#7cb445"/><circle cx="8" cy="7" r="2.6" fill="#fff"/></svg>
        Col. Lomas del Viento, Carretera a Tela a 200mts del Centro Comunal.
      </p>
      <p class="contact-line">
        Puerto Cortés, Honduras.
        <svg class="contact-icon" viewBox="0 0 16 20" aria-hidden="true"><path d="M8 0a7 7 0 0 0-7 7c0 5 7 13 7 13s7-8 7-13a7 7 0 0 0-7-7z" fill="#7cb445"/><circle cx="8" cy="7" r="2.6" fill="#fff"/></svg>
        minimarkettavo@correo-ejemplo.hn
        <svg class="contact-icon" viewBox="0 0 16 20" aria-hidden="true"><path d="M8 0a7 7 0 0 0-7 7c0 5 7 13 7 13s7-8 7-13a7 7 0 0 0-7-7z" fill="#7cb445"/><circle cx="8" cy="7" r="2.6" fill="#fff"/></svg>
        (504) 9731-5064
      </p>
    </footer>
  </section>
</body>
</html>
```